TrueLane Collision Repair Web Site

Create a web site that will inform my potential customers about the services I provide. We are a Automotive Collision repair business that uses the latest state of the art equipment, computerized paint matching highly trained technicians, have over 30 years experience. We work with all all insurance programs. Our Moto is "Fixed Right, The First Time, Every Time". TrueLane, The intelligent choice in collision repair.

Target Market(s)

People that have been in a auto collision, needs windshield replaced, people that drive 10 year or newer cars

Industry/Entity Type

Automotive

Coding

Coded - Design and coding required

Number of Pages Required

4 page

Font styles to use
Sans Serif

Requirements
Must have
• Logo, Place for Phone number, I need to be able to put the code in so I can use a tracking phone number
• site needs to be mobile ready or adaptive
• May want to have a photo of a high end car
• here is a web site for example with the pages that I want
• https://www.brisvaleautobody.example/online-repair-estimate,
• https://www.brisvaleautobody.example/schedule-appointment
• https://www.brisvaleautobody.example/collision-repair/auto-body-repair
• https://www.brisvaleautobody.example/contact
Nice to have
• Be great if the Car in the log could have the front damaged then have it fix in a animation. Not sure if could be done here

```html
<!DOCTYPE html>
<html lang="en">
<head>
<meta charset="utf-8">
<title>TrueLane Collision Repair</title>
<link rel="stylesheet" href="https://fonts.googleapis.com/css2?family=Cinzel:wght@400;700&family=Open+Sans:wght@400;600;700&display=swap">
<style>
:root{
  --red:#e31e26;
  --red-dark:#c4161d;
  --blue:#1a56a6;
  --blue-deep:#174f98;
  --navy:#2b3e5c;
  --ink:#222;
  --text:#555;
  --line:#dcdcdc;
  --tile:#ececec;
  --tile-edge:#cfcfcf;
  --seal:#e0b03a;
}
*{box-sizing:border-box;margin:0;padding:0}
html,body{width:929px;height:1200px;overflow:hidden;background:#fff}
body{position:relative;font-family:"Open Sans",Arial,sans-serif;color:var(--text)}
.abs{position:absolute}
a{color:inherit;text-decoration:none}

.topline{left:0;top:0;width:929px;height:3px;background:var(--blue)}
.brand{left:76px;top:22px;font-family:"Cinzel",serif;font-weight:700;color:var(--blue);line-height:1}
.brand .name{font-size:27px;display:block}
.brand .sub{font-size:11px;display:block;margin-top:4px;letter-spacing:.5px}
.callus{right:77px;top:17px;font-family:"Cinzel",serif;font-size:11px;color:#444;display:flex;align-items:center;gap:6px}
.callus b{font-family:"Open Sans",sans-serif;color:var(--red);font-size:15px;font-weight:700}
.nav{left:307px;top:54px;display:flex;gap:16px;font-family:"Cinzel",serif;font-size:12px;color:#222;font-weight:400;align-items:center;white-space:nowrap}
.nav .on{color:var(--red);position:relative}
.nav .on::after{content:"";position:absolute;left:50%;margin-left:-6px;top:16px;border:6px solid transparent;border-bottom-color:var(--red)}

.hero{left:0;top:82px;width:929px;height:296px;background:linear-gradient(90deg,#5d6670 0%,#8d959d 35%,#b7bcc1 60%,#9aa3ad 100%)}
.hero-text{left:75px;top:143px;font-family:"Cinzel",serif;font-weight:400;color:#fff;font-size:17.5px;line-height:32px;text-shadow:0 1px 3px rgba(0,0,0,.5)}
.btn{display:inline-flex;align-items:center;justify-content:center;color:#fff;font-weight:700;font-size:11px;border-radius:8px;white-space:nowrap}
.btn-red{background:linear-gradient(#ee2b31,var(--red-dark))}
.btn-blue{background:linear-gradient(#2766b8,var(--blue-deep))}
.hero .btn{position:absolute;left:76px;top:198px;width:129px;height:32px}
.dots{left:437px;top:344px;display:flex;gap:4px}
.dots i{width:10px;height:10px;background:#fff}
.dots i:first-child{background:var(--red);border:1px solid #fff}

.card{top:397px;width:247px;height:128px;border:3px solid #fff;outline:1px solid var(--line);color:#fff;text-align:center;padding-top:20px}
.card h3{font-family:"Cinzel",serif;font-weight:400;font-size:14.5px;margin-bottom:12px}
.card p{font-size:9.3px;line-height:16px;padding:0 24px}
.card .more{display:block;margin-top:10px;font-size:9.5px;font-weight:700}
.c1{left:76px;background:linear-gradient(135deg,#2d64ad,#1b4f97)}
.c2{left:341px;background:linear-gradient(135deg,#555,#222)}
.c3{left:605px;background:linear-gradient(135deg,#e02a2f,#c5161c)}

.rule{left:76px;width:777px;height:1px;background:var(--line)}

.services h2{position:absolute;left:76px;top:594px;font-family:"Cinzel",serif;font-weight:400;font-size:17px;color:var(--ink);white-space:nowrap}
.p1{left:76px;top:630px;width:320px;font-size:9.3px;line-height:18px}
.p2{left:76px;top:718px;width:420px;font-size:9.3px;line-height:18px}
.seal{left:400px;top:624px;width:92px;height:92px;border-radius:50%;background:var(--seal)}
.acts{left:76px;top:771px;display:flex;gap:12px}
.acts .btn{height:35px;padding:0 12px;font-size:10px}

.menu{left:553px;top:582px}
.menu li{list-style:none;position:absolute;left:0;width:275px;height:42px;background:var(--tile);border:2px solid var(--tile-edge);display:flex;align-items:center;gap:10px;padding-left:18px;font-size:11.5px;font-weight:600;color:#555}
.menu li.active{background:var(--red);border-color:var(--red);color:#fff;width:255px}
.menu .tip{position:absolute;left:253px;top:-2px;border-top:21px solid transparent;border-bottom:21px solid transparent;border-left:27px solid var(--red)}

.partners{left:0;top:877px;width:929px;height:57px}
.partner{position:absolute;top:0;width:119px;height:57px;border:1px solid #d5d5d5;background:#fff;display:flex;align-items:center;justify-content:center}
.partner span{width:70px;height:18px;background:#e6e6e6;border-radius:3px}
.arrow{position:absolute;top:20px}

.footer{left:0;top:970px;width:929px;height:177px;background:var(--navy);color:#fff}
.f-brand{position:absolute;left:76px;top:93px;font-family:"Cinzel",serif;font-weight:700;line-height:1}
.f-brand .name{font-size:26px;display:block}
.f-brand .sub{font-size:12px;display:block;margin-top:4px}
.col{position:absolute;top:24px;height:140px;border-left:1px solid rgba(255,255,255,.12);padding-left:36px}
.col h4{font-family:"Cinzel",serif;font-weight:400;font-size:13.5px;margin-bottom:12px;letter-spacing:.5px}
.col li{list-style:none;font-size:9.3px;line-height:18px;color:#dde3ec}
.bottom{left:0;top:1147px;width:929px;height:53px;background:var(--blue-deep);color:#fff}
.copy{position:absolute;left:77px;top:19px;font-size:9.3px}
.social{position:absolute;right:76px;top:13px;display:flex;gap:4px}
.social i{width:26px;height:26px;border:1.5px solid #fff;border-radius:50%}
</style>
</head>
<body>
<div class="abs topline"></div>

<header>
  <a class="abs brand" href="#"><span class="name">TRUELANE</span><span class="sub">COLLISION REPAIR</span></a>
  <div class="abs callus">
    <svg width="12" height="12" viewBox="0 0 24 24" aria-hidden="true"><path fill="#444" d="M6.6 10.8a15 15 0 006.6 6.6l2.2-2.2c.3-.3.7-.4 1-.2 1.1.4 2.3.6 3.6.6.6 0 1 .4 1 1V20c0 .6-.4 1-1 1A17 17 0 013 4c0-.6.4-1 1-1h3.5c.6 0 1 .4 1 1 0 1.3.2 2.5.6 3.6.1.3 0 .7-.2 1z"/></svg>
    CALL US ON : <b>1 800 555 0142</b>
  </div>
  <nav class="abs nav">
    <a class="on" href="#">HOME</a><a href="#">COLLISION REPAIR</a><a href="#">AUTO BODY</a><a href="#">AUTO GLASS</a><a href="#">EMPLOYMENT</a><a href="https://www.brisvaleautobody.example/contact">CONTACT</a>
    <svg width="11" height="11" viewBox="0 0 24 24" aria-hidden="true"><circle cx="10" cy="10" r="7" fill="none" stroke="#222" stroke-width="3"/><path d="M15 15l6 6" stroke="#222" stroke-width="3"/></svg>
  </nav>
</header>

<section class="abs hero" role="img" aria-label="Technician in blue overalls mounting a wheel alignment target on a car in the workshop">
  <a class="btn btn-red" href="https://www.brisvaleautobody.example/online-repair-estimate">GET AN ESTIMATE</a>
</section>
<h1 class="abs hero-text">FIX RIGHT, THE FIRST TIME,<br>EVERY TIME. &amp; TRUELANE,<br>THE INTELLIGENT CHOICE<br>IN COLLISION REPAIR</h1>
<div class="abs dots"><i></i><i></i><i></i><i></i></div>

<article class="abs card c1" role="img" aria-label="Mechanic working on a car wheel, blue tint">
  <h3>COLLISION REPAIR</h3>
  <p>Nemo enim ipsam voluptatem quia voluptas sit aspernatur aut odit aquia co</p>
  <a class="more" href="#">READ MORE &gt;&gt;</a>
</article>
<article class="abs card c2" role="img" aria-label="Auto body workshop with lifted cars, dark tint">
  <h3>AUTO BODY REPAIR</h3>
  <p>Nemo enim ipsam voluptatem quia voluptas sit aspernatur aut odit aquia co</p>
  <a class="more" href="https://www.brisvaleautobody.example/collision-repair/auto-body-repair">READ MORE &gt;&gt;</a>
</article>
<article class="abs card c3" role="img" aria-label="Red car detail, red tint">
  <h3>NEVER MISS AN OFFER!</h3>
  <p>Nemo enim ipsam voluptatem quia voluptas sit aspernatur aut odit aquia co</p>
  <a class="more" href="#">READ MORE &gt;&gt;</a>
</article>

<div class="abs rule" style="top:554px"></div>

<section class="services">
  <h2>AUTO BODY AND COLLISION REPAIR SERVICES.</h2>
  <p class="abs p1">At vero eos et accusamus et iusto odio dignissimos ducimus qui bland itiis praesentium voluptat um deleniti atque corrupti quos dolores et quas molestias excepturi sint occaecati cupiditatepro vident, similiqu sunt in culpa qui officia deserunt molliti..</p>
  <div class="abs seal" role="img" aria-label="Lifetime guarantee badge"></div>
  <p class="abs p2">Nam libero tempore, cum soluta nobis est eligendi optio cumque nihil impedit quo minus id quod maxime placeat facere possnis dolor repellendus.</p>
  <div class="abs acts">
    <a class="btn btn-red" href="https://www.brisvaleautobody.example/schedule-appointment">SCHEDULE APPOINTMENT</a>
    <a class="btn btn-blue" href="#">WHY CHOOSE TRUELANE</a>
  </div>
</section>

<ul class="abs menu">
  <li class="active" style="top:0"><svg width="11" height="15" viewBox="0 0 12 16" aria-hidden="true"><path fill="#fff" d="M6 0a6 6 0 00-6 6c0 4.5 6 10 6 10s6-5.5 6-10a6 6 0 00-6-6zm0 8.5A2.5 2.5 0 116 3.5a2.5 2.5 0 010 5z"/></svg>FIND A LOCATION<span class="tip"></span></li>
  <li style="top:46px"><svg width="15" height="15" viewBox="0 0 24 24" aria-hidden="true"><path fill="#666" d="M6.6 10.8a15 15 0 006.6 6.6l2.2-2.2c.3-.3.7-.4 1-.2 1.1.4 2.3.6 3.6.6.6 0 1 .4 1 1V20c0 .6-.4 1-1 1A17 17 0 013 4c0-.6.4-1 1-1h3.5c.6 0 1 .4 1 1 0 1.3.2 2.5.6 3.6.1.3 0 .7-.2 1z"/></svg>CUSTOMER SUPPORT</li>
  <li style="top:90px"><svg width="15" height="15" viewBox="0 0 24 24" aria-hidden="true"><circle cx="12" cy="12" r="11" fill="#666"/><path d="M9 9a3 3 0 116 0c0 2-3 2-3 4.5" stroke="#fff" stroke-width="2.4" fill="none"/><circle cx="12" cy="18" r="1.4" fill="#fff"/></svg>FREQUENTLY ASKED QUESTIONS</li>
  <li style="top:136px"><svg width="18" height="15" viewBox="0 0 26 22" aria-hidden="true"><rect x="2" y="4" width="16" height="16" rx="2" fill="none" stroke="#666" stroke-width="2.4"/><path d="M10 13l11-11 3 3-11 11-4 1z" fill="#666"/></svg>COLLISION ESTIMATE</li>
  <li style="top:180px"><svg width="18" height="15" viewBox="0 0 26 22" aria-hidden="true"><ellipse cx="10" cy="8" rx="9" ry="6.5" fill="none" stroke="#666" stroke-width="2.2"/><path d="M4 13l-2 5 6-3" fill="#666"/><path d="M19 6c4 1 6 3 6 6 0 2-1 3-2 4l1 4-4-2c-3 1-7 0-9-2" fill="none" stroke="#666" stroke-width="2"/></svg>FEEDBACK</li>
</ul>

<div class="abs rule" style="top:838px"></div>

<section class="abs partners" aria-label="Partners">
  <svg class="arrow" style="left:76px" width="12" height="18" viewBox="0 0 12 18" aria-hidden="true"><path d="M10 2L3 9l7 7" fill="none" stroke="#999" stroke-width="2"/></svg>
  <div class="partner" style="left:141px"><span></span></div>
  <div class="partner" style="left:273px"><span></span></div>
  <div class="partner" style="left:405px"><span></span></div>
  <div class="partner" style="left:536px"><span></span></div>
  <div class="partner" style="left:668px"><span></span></div>
  <svg class="arrow" style="left:842px" width="12" height="18" viewBox="0 0 12 18" aria-hidden="true"><path d="M2 2l7 7-7 7" fill="none" stroke="#999" stroke-width="2"/></svg>
</section>

<footer class="abs footer">
  <div class="f-brand"><span class="name">TRUELANE</span><span class="sub">COLLISION REPAIR</span></div>
  <div class="col" style="left:258px;width:155px"><h4>ABOUT US</h4><ul><li>Our Story</li><li>Team</li><li>Newsletters</li><li>Contact</li><li>Jobs</li><li>Help Us Grow</li></ul></div>
  <div class="col" style="left:416px;width:150px"><h4>SUPPORT</h4><ul><li>System Status</li><li>Forum</li><li>Help Center</li><li>Contact Us</li></ul></div>
  <div class="col" style="left:565px;width:170px"><h4>RESOURCES</h4><ul><li>Roadmap &amp; Updates</li><li>Security</li><li>Privacy Policy</li><li>Terms of Service</li><li>Webinars</li><li>Free for Startups</li></ul></div>
  <div class="col" style="left:741px;width:150px"><h4>LEGAL</h4><ul><li>Certified Trainers</li><li>Teamwork</li><li>Developer Zone</li><li>Referral Program</li><li>Refund Policy</li><li>Login</li></ul></div>
</footer>
<div class="abs bottom">
  <p class="copy">Copyrights © 2016, TrueLane. All rights reserved.</p>
  <div class="social" aria-label="Social links"><i></i><i></i><i></i><i></i></div>
</div>
</body>
</html>
```